Flag Order

We were just looking to order some branding flags to put on our rental equipment for our business. We would like different examples of the colors, shapes, sizes, backgrounds etc. Was thinking of just doing the plains icon instead of the whole logo on there. but open to ideas. preferably not a white background as they could get dirty,

```html
<!DOCTYPE html>
<html lang="en">
<head>
<meta charset="utf-8">
<title>Mesa Equipment Rentals: Flag Concepts</title>
<link rel="stylesheet" href="https://fonts.googleapis.com/css2?family=Archivo+Black&family=Montserrat:wght@400;700&display=swap">
<style>
  :root {
    --flag-blue: #1a7bd0;
    --ink: #222222;
    --white: #ffffff;
    --label-grey: #8a8a8a;
    --pole: #000000;
    --base-grey: #9a9a9a;
  }
  html, body {
    margin: 0;
    padding: 0;
    overflow: hidden;
    background: var(--white);
  }
  .canvas {
    position: relative;
    width: 1200px;
    height: 800px;
    overflow: hidden;
    background: var(--white);
  }
  .hardware {
    position: absolute;
    inset: 0;
  }
  .design-label {
    position: absolute;
    margin: 0;
    font-family: "Montserrat", sans-serif;
    font-weight: 400;
    font-size: 11.5px;
    letter-spacing: 4px;
    color: var(--label-grey);
    transform: translateX(-50%);
    white-space: nowrap;
  }
  .flag {
    position: absolute;
    background: var(--flag-blue);
    display: flex;
    align-items: center;
    justify-content: center;
  }
  .brand-name {
    font-family: "Archivo Black", sans-serif;
    color: var(--ink);
    line-height: 0.9;
    letter-spacing: 1px;
  }
  .brand-tagline {
    font-family: "Montserrat", sans-serif;
    font-weight: 700;
    color: var(--white);
    text-transform: uppercase;
    white-space: nowrap;
  }
  .brand-mark {
    background: var(--white);
    flex: none;
  }
  .lockup {
    display: flex;
    flex-direction: column;
    align-items: center;
  }

  /* Design 1 — tall feather flag, vertical lockup */
  .flag-feather-tall {
    left: 100px; top: 98px; width: 140px; height: 559px;
  }
  .flag-feather-tall .rotated {
    position: absolute;
    left: 50%; top: 50%;
    width: 559px; height: 140px;
    transform: translate(-50%, -50%) rotate(-90deg);
    display: flex;
    align-items: center;
    justify-content: center;
    gap: 40px;
  }
  .flag-feather-tall .brand-mark { width: 70px; height: 70px; }
  .flag-feather-tall .lockup { align-items: flex-start; }
  .flag-feather-tall .brand-name { font-size: 108px; }
  .flag-feather-tall .brand-tagline { font-size: 19px; letter-spacing: 8.5px; margin-top: 10px; }

  /* Design 2 — horizontal banner, full lockup */
  .flag-banner-full {
    left: 302px; top: 112px; width: 274px; height: 169px;
    flex-direction: column;
    gap: 14px;
  }
  .flag-banner-full .brand-mark { width: 54px; height: 54px; }
  .flag-banner-full .brand-name { font-size: 34px; }
  .flag-banner-full .brand-tagline { font-size: 7.5px; letter-spacing: 2.6px; margin-top: 4px; }

  /* Design 3 — horizontal banner, name only */
  .flag-banner-mark {
    left: 616px; top: 112px; width: 275px; height: 168px;
    gap: 18px;
  }
  .flag-banner-mark .brand-mark { width: 44px; height: 44px; }
  .flag-banner-mark .brand-name { font-size: 60px; }

  /* Design 4 — short feather flag, full lockup */
  .flag-feather-full {
    left: 778px; top: 420px; width: 141px; height: 233px;
    flex-direction: column;
    gap: 14px;
  }
  .flag-feather-full .brand-mark { width: 56px; height: 56px; }
  .flag-feather-full .brand-name { font-size: 30px; }
  .flag-feather-full .brand-tagline { font-size: 6.8px; letter-spacing: 2.2px; margin-top: 4px; }

  /* Design 5 — short feather flag, name only */
  .flag-feather-mark {
    left: 1020px; top: 420px; width: 140px; height: 233px;
    flex-direction: column;
    gap: 16px;
  }
  .flag-feather-mark .brand-mark { width: 44px; height: 44px; }
  .flag-feather-mark .brand-name { font-size: 40px; }
</style>
</head>
<body>
<main class="canvas">

  <svg class="hardware" width="1200" height="800" viewBox="0 0 1200 800" aria-hidden="true">
    <defs>
      <g id="stand-base">
        <rect x="-5" y="-8" width="10" height="14" fill="#c8c8c8" stroke="#777" stroke-width="1"/>
        <line x1="0" y1="4" x2="-68" y2="10" stroke="var(--base-grey)" stroke-width="2"/>
        <line x1="0" y1="4" x2="42" y2="-8" stroke="var(--base-grey)" stroke-width="2"/>
        <line x1="0" y1="4" x2="-40" y2="40" stroke="var(--base-grey)" stroke-width="2"/>
        <line x1="0" y1="4" x2="78" y2="28" stroke="var(--base-grey)" stroke-width="2"/>
      </g>
    </defs>

    <!-- Design 1 hardware -->
    <rect x="92" y="100" width="8" height="560" fill="var(--pole)"/>
    <path d="M92 104 Q92 97 100 97 L240 97 L240 100 L100 100 Z" fill="var(--pole)"/>
    <rect x="94" y="660" width="5" height="48" fill="var(--pole)"/>
    <use href="#stand-base" x="97" y="718"/>

    <!-- Design 2 hardware -->
    <circle cx="298" cy="102" r="7" fill="var(--pole)"/>
    <rect x="294" y="104" width="8" height="556" fill="var(--pole)"/>
    <rect x="296" y="660" width="5" height="48" fill="var(--pole)"/>
    <use href="#stand-base" x="298" y="718"/>

    <!-- Design 3 hardware -->
    <circle cx="613" cy="102" r="7" fill="var(--pole)"/>
    <rect x="608" y="104" width="8" height="556" fill="var(--pole)"/>
    <rect x="610" y="660" width="5" height="48" fill="var(--pole)"/>
    <use href="#stand-base" x="612" y="718"/>

    <!-- Design 4 hardware -->
    <rect x="772" y="422" width="6" height="238" fill="var(--pole)"/>
    <path d="M772 425 Q772 418 779 418 L919 418 L919 421 L778 421 Z" fill="var(--pole)"/>
    <rect x="773" y="660" width="4" height="48" fill="var(--pole)"/>
    <use href="#stand-base" x="775" y="718"/>

    <!-- Design 5 hardware -->
    <rect x="1014" y="422" width="6" height="238" fill="var(--pole)"/>
    <path d="M1014 425 Q1014 418 1021 418 L1160 418 L1160 421 L1020 421 Z" fill="var(--pole)"/>
    <rect x="1015" y="660" width="4" height="48" fill="var(--pole)"/>
    <use href="#stand-base" x="1017" y="718"/>
  </svg>

  <p class="design-label" style="left:161px; top:50px;">DESIGN #1</p>
  <p class="design-label" style="left:440px; top:50px;">DESIGN #2</p>
  <p class="design-label" style="left:758px; top:50px;">DESIGN #3</p>
  <p class="design-label" style="left:846px; top:368px;">DESIGN #4</p>
  <p class="design-label" style="left:1087px; top:368px;">DESIGN #5</p>

  <section class="flag flag-feather-tall">
    <div class="rotated">
      <span class="brand-mark"></span>
      <div class="lockup">
        <span class="brand-name">MESA</span>
        <span class="brand-tagline">Equipment Rentals</span>
      </div>
    </div>
  </section>

  <section class="flag flag-banner-full">
    <span class="brand-mark"></span>
    <div class="lockup">
      <span class="brand-name">MESA</span>
      <span class="brand-tagline">Equipment Rentals</span>
    </div>
  </section>

  <section class="flag flag-banner-mark">
    <span class="brand-mark"></span>
    <span class="brand-name">MESA</span>
  </section>

  <section class="flag flag-feather-full">
    <span class="brand-mark"></span>
    <div class="lockup">
      <span class="brand-name">MESA</span>
      <span class="brand-tagline">Equipment Rentals</span>
    </div>
  </section>

  <section class="flag flag-feather-mark">
    <span class="brand-mark"></span>
    <span class="brand-name">MESA</span>
  </section>

</main>
</body>
</html>
```